Trvmlegal.com needs a wedsite. Law Office of Darnell P. Whitby

Darnell P. Whitby is a criminal law firm that is 5 years old. We have already had all the content written and now just need the website designed. We also just finished our logo design using Pixel Harbor and would like it used in the design of the website.

Industry/Entity Type

Law Firm

Number of Pages Required

5+ page

Requirements
Must have
• I was our new logo to be on the website also. I want Dallas sites as the stock pictures for the website. For example the Grey Stone Tribunal. I also need to be able to add YouTube videos. It has to adjust to be seen on computers and also cell phones. I need to be able to have a information sheet for clients to fill out and submit back to me.

```html
<!DOCTYPE html>
<html lang="en">
<head>
<meta charset="utf-8">
<title>Law Office of Darnell P. Whitby</title>
<link href="https://fonts.googleapis.com/css2?family=Montserrat:wght@400;500;600&family=Roboto:wght@400;500&display=swap" rel="stylesheet">
<style>
:root{
  --navy:#0c1f5e;
  --navy-deep:#06154a;
  --black:#111111;
  --footer:#1b1b1b;
  --grey-band:#ebebeb;
  --text:#444444;
  --muted:#777777;
  --gold:#d8a422;
  --white:#ffffff;
}
*{margin:0;padding:0;box-sizing:border-box}
html,body{width:722px;height:1200px;overflow:hidden;background:var(--white)}
body{position:relative;font-family:'Roboto',Arial,sans-serif;color:var(--text)}
.abs{position:absolute}
.head-font{font-family:'Montserrat',Arial,sans-serif}
.top-rule{left:0;top:0;width:722px;height:2px;background:var(--navy)}
.brand{left:66px;top:11px;display:flex;align-items:center;gap:8px}
.brand-dot{width:58px;height:58px;border-radius:50%;background:var(--navy)}
.brand-name{font-family:'Montserrat',sans-serif;font-weight:600;font-size:11px;color:var(--navy);line-height:1.3;width:110px}
.call{right:68px;top:18px;font-size:10px;color:#222;display:flex;align-items:center;gap:4px}
.search{left:542px;top:40px;width:112px;height:24px;background:#eeeeee;font-size:7.5px;color:#999;padding:0 10px;display:flex;align-items:center;justify-content:space-between}
.nav{left:67px;top:75px;width:587px;height:33px;background:var(--black);display:flex}
.nav a{color:var(--white);font-family:'Montserrat',sans-serif;font-size:7.5px;text-decoration:none;display:flex;align-items:center;justify-content:center;height:100%}
.nav a.active{background:var(--navy)}
.hero{left:0;top:113px;width:722px;height:321px;background:linear-gradient(90deg,#4a3c30 0%,#8a7765 30%,#a89684 55%,#7c6a5a 80%,#3e3128 100%)}
.hero-title{left:0;top:218px;width:722px;text-align:center;font-family:'Montserrat',sans-serif;font-weight:500;font-size:25px;color:var(--white);text-shadow:0 1px 3px rgba(0,0,0,.4)}
.hero-text{left:120px;top:252px;width:482px;text-align:center;font-size:8.3px;line-height:15.5px;color:var(--white);text-shadow:0 1px 2px rgba(0,0,0,.5)}
.hero-arrows{left:339px;top:296px;width:44px;height:44px;border-radius:50%;background:var(--white)}
.intro-title{left:0;top:457px;width:722px;text-align:center;font-family:'Montserrat',sans-serif;font-weight:500;font-size:12.5px;color:var(--navy)}
.intro-text{left:60px;top:476px;width:602px;text-align:center;font-size:7.1px;line-height:15.5px;color:#333}
.btn{left:318px;top:562px;width:86px;height:30px;border-radius:15px;background:var(--navy-deep);color:var(--white);font-family:'Montserrat',sans-serif;font-size:7px;display:flex;align-items:center;justify-content:center;box-shadow:0 2px 3px rgba(0,0,0,.3)}
.band{left:0;top:606px;width:722px;height:209px;background:var(--grey-band)}
.team{left:67px;top:606px;width:186px;height:209px;background:var(--black);padding:14px 13px}
.team h2{font-family:'Montserrat',sans-serif;font-weight:500;font-size:13px;color:var(--white);margin-bottom:9px}
.member{display:flex;gap:7px;height:57px}
.avatar{width:40px;height:40px;border-radius:50%;border:2px solid var(--white);background:linear-gradient(180deg,#c9d3df,#2b3a55);flex:none}
.member h3{font-family:'Montserrat',sans-serif;font-weight:500;font-size:8px;color:var(--gold);margin:2px 0 3px}
.member p{font-size:6.5px;line-height:12.5px;color:#666}
.help-title{left:267px;top:619px;font-family:'Montserrat',sans-serif;font-weight:500;font-size:13px;color:var(--navy)}
.svc{width:187px}
.svc h3{font-family:'Montserrat',sans-serif;font-weight:500;font-size:8.6px;color:#222;margin-bottom:5px}
.svc p{font-size:6.7px;line-height:14.5px;color:#555;height:44px}
.more{font-family:'Montserrat',sans-serif;font-weight:600;font-size:6.4px;color:var(--navy);display:flex;align-items:center;gap:2px}
.svc .more{justify-content:flex-end;padding:3px 0 6px;border-bottom:1px solid #aaa}
.news-title{left:0;top:836px;width:722px;text-align:center;font-family:'Montserrat',sans-serif;font-weight:500;font-size:12.5px;color:var(--navy)}
.news{width:285px}
.news-img{height:108px}
.news .date{font-size:6.8px;font-style:italic;color:var(--navy);margin:14px 0 5px}
.news h3{font-family:'Montserrat',sans-serif;font-weight:400;font-size:9px;color:#222;margin-bottom:5px}
.news p{font-size:6.5px;line-height:12.5px;color:#555;margin-bottom:4px}
.follow{left:0;top:1075px;width:722px;height:80px;background:var(--navy)}
.follow h2{text-align:center;font-family:'Montserrat',sans-serif;font-weight:500;font-size:12px;color:var(--white);margin-top:16px}
.socials{display:flex;justify-content:center;gap:7px;margin-top:10px}
.socials span{width:24px;height:24px;border-radius:50%;background:#141414;display:block}
.footer{left:0;top:1155px;width:722px;height:45px;background:var(--footer);font-size:6.5px;color:#aaa}
.footer .links{position:absolute;left:67px;top:19px}
.footer .copy{position:absolute;right:67px;top:19px}
</style>
</head>
<body>
<div class="abs top-rule"></div>

<header>
  <div class="abs brand">
    <div class="brand-dot"></div>
    <div class="brand-name">Darnell P. Whitby</div>
  </div>
  <div class="abs call">
    <svg width="9" height="9" viewBox="0 0 10 10"><rect width="10" height="10" rx="2" fill="#0c1f5e"/><path d="M3 2.3l1 1.6-.6.7c.4.9 1 1.5 1.9 1.9l.7-.6 1.6 1-.5 1.1C5 7.8 2.2 5 2 3z" fill="#fff"/></svg>
    CALL US : 214.555.0148
  </div>
  <div class="abs search">Search...
    <svg width="7" height="7" viewBox="0 0 10 10"><circle cx="4" cy="4" r="3" fill="none" stroke="#555" stroke-width="1.6"/><path d="M6.2 6.2L9 9" stroke="#555" stroke-width="1.8"/></svg>
  </div>
  <nav class="abs nav">
    <a class="active" style="width:75px">HOME</a>
    <a style="width:74px">OUR PROFILE</a>
    <a style="width:65px">SERVICES</a>
    <a style="width:106px">HOW WE CAN HELP</a>
    <a style="width:95px">NEWS &amp; EVENTS</a>
    <a style="width:120px">CONTACT US</a>
  </nav>
</header>

<section>
  <div class="abs hero" role="img" aria-label="Photo of stone courthouse columns"></div>
  <h1 class="abs hero-title">LAW OFFICE OF DARNELL P. WHITBY</h1>
  <p class="abs hero-text">Lorem ipsum dolor sit amet, consectetuer adipiscing elit, sed diam nonummy nibh euismod tincidunt ut laoreet dolore magna aliquam erat volutpat. Ut wisi enim ad minim veniam, quis nostrud exerci tation ullamcorper.</p>
  <div class="abs hero-arrows">
    <svg width="44" height="44" viewBox="0 0 44 44"><path d="M18 16l-5 6 5 6M26 16l5 6-5 6" fill="none" stroke="#0c1f5e" stroke-width="3" stroke-linecap="round" stroke-linejoin="round"/></svg>
  </div>
</section>

<section>
  <h2 class="abs intro-title">OUR AGGRESSIVE CRIMINAL DEFENSE TEAM FIGHTS FOR YOU</h2>
  <p class="abs intro-text">You are innocent unless proven guilty. But our criminal justice system often unjustly denies this fundamental constitutional right. The Law Office of Darnell P. Whitby seeks to balance the scales of justice. Our Dallas-Fort Worth law firm solely handles criminal defense cases so we can dedicate our full resources to the pursuit of justice. Our criminal defense attorneys presume that every case we take will go to trial and aggressively advocate for you from the moment we take your case. Because the wheels of justice spin 24 hours, so do we. If you are arrested after-hours, on weekends or on holidays, we are available to handle your jail release.<br>Call the Law Office of Darnell P. Whitby at 214.555.0148 or contact us online for zealous, experienced representation.</p>
  <div class="abs btn">CONTACT NOW</div>
</section>

<section>
  <div class="abs band"></div>
  <div class="abs team">
    <h2>MEET OUR &nbsp;TEAM</h2>
    <div class="member"><div class="avatar" role="img" aria-label="Portrait of Darnell P. Whitby"></div><div><h3>DARNELL P. WHITBY</h3><p>Lorem ipsum dolor sit amet, consec tetuer adipiscing elit.</p></div></div>
    <div class="member"><div class="avatar" role="img" aria-label="Portrait of Marisol Quentry-Vale"></div><div><h3>MARISOL QUENTRY-VALE</h3><p>Ut wisi enim ad minim veniam, quis nostrud exerci tation.</p></div></div>
    <div class="member"><div class="avatar" role="img" aria-label="Portrait of Tobin Harlowe"></div><div><h3>TOBIN HARLOWE</h3><p>Duis autem vel eum iriure dolor in hendrerit in vulputate.</p></div></div>
  </div>

  <h2 class="abs help-title">HOW WE CAN HELP</h2>
  <div class="abs svc" style="left:267px;top:643px">
    <h3>MURDER &amp; OTHER HOMICIDE OFFENSES</h3>
    <p>Lorem ipsum dolor sit amet, consectetuer adipiscing elit, sed diam nonummy nibh euismod tincidunt ut laoreet dolore magna aliquam erat volutpat.</p>
    <div class="more">READ MORE <svg width="6" height="6" viewBox="0 0 6 6"><circle cx="3" cy="3" r="3" fill="#0c1f5e"/><path d="M2.3 1.6L3.7 3 2.3 4.4" fill="none" stroke="#fff" stroke-width="1"/></svg></div>
  </div>
  <div class="abs svc" style="left:468px;top:643px">
    <h3>SEXUAL OFFENSES</h3>
    <p>Ut wisi enim ad minim veniam, quis nostrud exerci tation ullamcorper suscipit lobortis nisl ut aliquip ex ea co mmodo consequat.</p>
    <div class="more">READ MORE <svg width="6" height="6" viewBox="0 0 6 6"><circle cx="3" cy="3" r="3" fill="#0c1f5e"/><path d="M2.3 1.6L3.7 3 2.3 4.4" fill="none" stroke="#fff" stroke-width="1"/></svg></div>
  </div>
  <div class="abs svc" style="left:267px;top:730px">
    <h3>EXPUNGEMENTS &amp; NON-DISCLOSURES</h3>
    <p>Duis autem vel eum iriure dolor in hendrerit in vulputate velit esse molestie consequat, vel illum dolore eu feugiat nulla facilisis at vero eros et accumsan.</p>
    <div class="more" style="border:0">READ MORE <svg width="6" height="6" viewBox="0 0 6 6"><circle cx="3" cy="3" r="3" fill="#0c1f5e"/><path d="M2.3 1.6L3.7 3 2.3 4.4" fill="none" stroke="#fff" stroke-width="1"/></svg></div>
  </div>
  <div class="abs svc" style="left:468px;top:730px">
    <h3>EARLY PROBATION RELEASE</h3>
    <p>Vel eum iriure dolor in hendrerit in vulputate velit esse molestie consequat, vel illum dolore eu feugiat nulla facilisis at vero eros et accumsan.</p>
    <div class="more" style="border:0">READ MORE <svg width="6" height="6" viewBox="0 0 6 6"><circle cx="3" cy="3" r="3" fill="#0c1f5e"/><path d="M2.3 1.6L3.7 3 2.3 4.4" fill="none" stroke="#fff" stroke-width="1"/></svg></div>
  </div>
</section>

<section>
  <h2 class="abs news-title">LATEST NEWS</h2>
  <article class="abs news" style="left:67px;top:863px">
    <div class="news-img" role="img" aria-label="Photo of a lawyer meeting with clients" style="background:linear-gradient(90deg,#b9c6d2,#d9e0e6 50%,#8a7c72)"></div>
    <div class="date">JAN 27, 2014</div>
    <h3>LOREM IPSUM DOLOR SIT AMET CONSEC</h3>
    <p>Aliquam dapibus tincidunt metus. Praesent justo dolor, lobortis quis, lobortis dignissim, pulvin ar ac, lorem. Lorem ipsum dolor sit amet, consectetuer adipiscing elit. Praesent vestibulum molestie lacus. Aenean nonummy hendrerit mauris....</p>
    <div class="more">READ MORE <svg width="6" height="6" viewBox="0 0 6 6"><circle cx="3" cy="3" r="3" fill="#0c1f5e"/><path d="M2.3 1.6L3.7 3 2.3 4.4" fill="none" stroke="#fff" stroke-width="1"/></svg></div>
  </article>
  <article class="abs news" style="left:368px;top:863px">
    <div class="news-img" role="img" aria-label="Photo of handcuffed hands" style="background:linear-gradient(90deg,#3a3a3a,#6d6d6d 50%,#404040)"></div>
    <div class="date">JAN 27, 2014</div>
    <h3>SED UT PERSPICIATIS UNDE OMNIS ISTE</h3>
    <p>Aliquam dapibus tincidunt metus. Praesent justo dolor, lobortis quis, lobortis dignissim, pulvin ar ac, lorem. Lorem ipsum dolor sit amet, consectetuer adipiscing elit. Praesent vestibulum molestie lacus. Aenean nonummy hendrerit mauris....</p>
    <div class="more">READ MORE <svg width="6" height="6" viewBox="0 0 6 6"><circle cx="3" cy="3" r="3" fill="#0c1f5e"/><path d="M2.3 1.6L3.7 3 2.3 4.4" fill="none" stroke="#fff" stroke-width="1"/></svg></div>
  </article>
</section>

<section class="abs follow">
  <h2>FOLLOW US ON</h2>
  <div class="socials">
    <span aria-label="Social profile"></span><span aria-label="Social profile"></span><span aria-label="Video channel"></span><span aria-label="Social profile"></span><span aria-label="News feed"></span>
  </div>
</section>

<footer class="abs footer">
  <div class="links">Home &nbsp;| &nbsp;About Us &nbsp;| &nbsp;Services &nbsp;| &nbsp;Contact Us &nbsp;| &nbsp;Privacy Policy</div>
  <div class="copy">Copyright @ 2015 DPW Law. All Right Reserved.</div>
</footer>
</body>
</html>
```